Recycling Depot Business Card Design

We need a double sided business card for our recycling depot business. Please include name, position, address, phone, cell, fax, email and website address. Business card should match the colour scheme of our logo and look environmental but modern. I've attached a few business cards from Mintvale Works that I like.

Industry/Entity Type

Recycling

Contact Information for Business Card

Please include name, position, address, phone, cell, fax, email and website address.

Font styles to use
Sans Serif

Requirements
Must have
• Our Logo, Colour Scheme that matches our logo. Use of Colour Gradients and a custom look.

```html
<!DOCTYPE html>
<html lang="en">
<head>
<meta charset="utf-8">
<title>Greenloop Depot Business Card</title>
<link href="https://fonts.googleapis.com/css2?family=Source+Sans+3:wght@400;600&display=swap" rel="stylesheet">
<style>
  :root {
    --page-bg: #d9d4cc;
    --card-clear: #eef0ee;
    --card-clear-edge: #dfe3e0;
    --green-deep: #0e3520;
    --green-mid: #2c5a3c;
    --green-bright: #4f9a2e;
    --green-accent: #3f8a26;
    --text-light: #e6eee8;
    --logo-green: #1f5a22;
  }
  * { margin: 0; padding: 0; box-sizing: border-box; }
  html, body { width: 1200px; height: 969px; overflow: hidden; }
  body {
    background: var(--page-bg);
    font-family: "Source Sans 3", sans-serif;
    position: relative;
  }
  .business-card {
    position: absolute;
    left: 120px; top: 211px;
    width: 960px; height: 546px;
    box-shadow: 0 10px 30px rgba(0,0,0,.18);
    overflow: hidden;
  }
  .card-art { position: absolute; inset: 0; }
  .contact-block {
    position: absolute;
    left: 46px; top: 116px;
    color: var(--text-light);
  }
  .person-name {
    font-size: 29px; font-weight: 600;
    color: var(--green-bright);
    line-height: 34px;
  }
  .person-title { font-size: 21px; line-height: 26px; }
  .address { margin-top: 34px; font-size: 21px; line-height: 27px; }
  .contact-list { list-style: none; margin-top: 14px; }
  .contact-list li {
    display: flex; align-items: center;
    font-size: 20px; line-height: 27.5px;
  }
  .contact-icon { width: 16px; height: 16px; margin-right: 14px; flex: none; }
  .brand {
    position: absolute;
    left: 470px; top: 238px;
    display: flex; align-items: center;
  }
  .brand-dot {
    width: 40px; height: 40px; border-radius: 50%;
    background: var(--green-accent);
    margin-right: 16px;
  }
  .brand-name {
    font-size: 52px; font-weight: 600;
    color: var(--logo-green);
    letter-spacing: -0.5px;
  }
</style>
</head>
<body>
  <div class="business-card">
    <svg class="card-art" width="960" height="546" viewBox="0 0 960 546">
      <defs>
        <linearGradient id="clearGrad" x1="0" y1="0" x2="1" y2="1">
          <stop offset="0" stop-color="#f4f6f4"/>
          <stop offset="1" stop-color="#dde2de"/>
        </linearGradient>
        <radialGradient id="greenGrad" cx="0.35" cy="0.75" r="0.9">
          <stop offset="0" stop-color="#356445"/>
          <stop offset="1" stop-color="#0e3520"/>
        </radialGradient>
        <linearGradient id="stripeGrad" x1="0" y1="0" x2="0" y2="1">
          <stop offset="0" stop-color="#8fc46a"/>
          <stop offset="1" stop-color="#2f7a1c"/>
        </linearGradient>
      </defs>
      <rect class="clear-side" width="960" height="546" fill="url(#clearGrad)"/>
      <path class="accent-stripe" d="M450 0 C385 80 355 220 380 330 C410 440 540 515 660 546 H623 C520 520 395 440 365 330 C340 220 370 80 433 0 Z" fill="url(#stripeGrad)"/>
      <path class="green-panel" d="M0 0 H433 C370 80 340 220 365 330 C395 440 520 520 623 546 H0 Z" fill="url(#greenGrad)"/>
    </svg>

    <div class="contact-block">
      <div class="person-name">Daniel Hartley</div>
      <div class="person-title">President</div>
      <div class="address">214 Willow Bend Road<br>Fairbanks, Alaska 99701</div>
      <ul class="contact-list">
        <li><svg class="contact-icon" viewBox="0 0 16 16"><path d="M3 1l3 3-2 2c1 2 3 4 5 5l2-2 3 3-2 3C6 15 1 10 1 3z" fill="#5aa63a"/></svg>555-214-7730</li>
        <li><svg class="contact-icon" viewBox="0 0 16 16"><rect x="4" y="0.5" width="8" height="15" rx="1.5" fill="none" stroke="#5aa63a" stroke-width="1.5"/></svg>555-318-4469</li>
        <li><svg class="contact-icon" viewBox="0 0 16 16"><rect x="4" y="1" width="8" height="5" fill="#5aa63a"/><rect x="1" y="6" width="14" height="7" rx="1" fill="#5aa63a"/></svg>555-402-9917</li>
        <li><svg class="contact-icon" viewBox="0 0 16 16"><rect x="1" y="3" width="14" height="10" fill="#5aa63a"/><path d="M1 3l7 6 7-6" fill="none" stroke="#0e3520" stroke-width="1.2"/></svg>info@greenloopdepot.com</li>
        <li><svg class="contact-icon" viewBox="0 0 16 16"><circle cx="8" cy="8" r="7" fill="#5aa63a"/><path d="M1 8h14M8 1c-3 4-3 10 0 14M8 1c3 4 3 10 0 14" fill="none" stroke="#0e3520" stroke-width="1"/></svg>www.greenloopdepot.com</li>
      </ul>
    </div>

    <div class="brand">
      <span class="brand-dot"></span>
      <span class="brand-name">Greenloop Depot</span>
    </div>
  </div>
</body>
</html>
```